Logo/ business card idea for a weld inspection/ nondestructive testing LLC

I have just started an LLC (my first) for weld inspection and non-destructive testing. I am the president and only member of this company. It is a very niche industry and word of mouth is basically the only advertisement needed to get you the next job. I will offer magnetic particle, dye penetrant, ultrasonic, and visual testing for the non-destructive services. X-ray is a form of non-destructive testing that I spent a few years doing but to costly for me at this time. All pipelines under the ground are welded, visually inspected and x-ray by someone just like me. All new building construction, any type of nuclear plant , pressure vessel, ect. , the welds are inspected by someone like me. Its is every increasing also with safety concerns. People are living right next to this stuff!!I will be the guy that fabrication shops or construction companies call to give the final OK that the welds are satisfactory after inspection to a certain code or standard. The designers have all the freedom they wish but I have attached a PDF with greater explanations and color ideas. I want raised glossy print on the front of the card and the necessary info. The back will not have raised print and serve more as a brief resume listing the certifications I have. The company only cares about the certifications and ultimately my signature. I want to make the front of the car into a fridge magnet to pass out with the card also. Something that is appealing to hang up instead of getting lost in someones wallet. The final design………. should be classic and stand the test of time. It should communicate precision and accuracy as well as incorporate the sound beam you will find in the PDF I’ve attached.Thanks and have a great day,Dwayne

Target Market(s)

Adult males in english speaking countries that handle welding and/or construction duties. Most of the time under heavy time constraints and deadlines. Ages 30-60

Industry/Entity Type

Construction

Contact Information for Business Card

Halvern Inspection Services, LLC
Dwayne Halvern
Ithaca, MI
989-517-2438
halv7dw@mailtrove.net

Font styles to use
Other font styles liked:
• designers choice

Requirements
Nice to have
• The logo on the front can completely encase the Halvern, be segmented incorporating the Halvern, or next to it. There can also be a couple of “flaws” (the red, blue and yellow in some of the pictures attached in the PDF) in the sound beam spread.

```html
<!DOCTYPE html>
<html lang="en">
<head>
<meta charset="utf-8">
<title>Halvern Inspection Services, LLC — Business Card</title>
<link rel="stylesheet" href="https://fonts.googleapis.com/css2?family=Nunito+Sans:wght@300;400&display=swap">
<style>
  :root {
    --bg: #a9a9a9;
    --card: #f1f1f1;
    --teal: #7dbfb4;
    --teal-deep: #6fb5aa;
    --orange: #e8692c;
    --ink: #4a4a4a;
    --white: #ffffff;
  }
  * { margin: 0; padding: 0; box-sizing: border-box; }
  html, body {
    width: 1200px; height: 1000px; overflow: hidden;
    background: var(--bg);
    font-family: "Nunito Sans", "Helvetica Neue", Arial, sans-serif;
  }
  .canvas { position: relative; width: 1200px; height: 1000px; }

  .card {
    position: absolute;
    width: 680px; height: 390px;
    background: var(--card);
    overflow: hidden;
  }
  .card--front { left: 90px; top: 95px; }
  .card--back { left: 430px; top: 515px; }

  /* Front */
  .wordmark {
    position: absolute; left: 190px; top: 120px;
    color: var(--teal); font-weight: 300; line-height: 1;
  }
  .wordmark__name { display: block; font-size: 92px; letter-spacing: 1px; }
  .wordmark__sub { display: block; font-size: 25px; margin-top: 6px; padding-left: 4px; }
  .wordmark-rule {
    position: absolute; left: 520px; right: 0; top: 188px;
    height: 2px; background: var(--orange);
  }
  .contact {
    position: absolute; left: 56px; bottom: 38px;
    font-size: 20px; color: var(--ink); font-weight: 400; letter-spacing: .3px;
  }
  .contact__sep { color: var(--orange); margin: 0 12px; }

  /* Back */
  .connector { position: absolute; left: 0; top: 0; width: 680px; height: 390px; }
  .cert {
    position: absolute; left: 78px; width: 575px; height: 102px;
    border: 2px solid var(--orange);
    display: flex; align-items: stretch;
  }
  .cert--society { top: 58px; }
  .cert--level { top: 178px; left: 70px; }
  .cert__title {
    background: var(--teal-deep); color: var(--white);
    font-weight: 300; font-size: 72px; line-height: 1;
    display: flex; align-items: center; padding: 0 16px;
  }
  .cert--society .cert__title { width: 212px; }
  .cert--level .cert__title { width: 315px; }
  .cert__list {
    list-style: none; color: var(--orange);
    font-size: 18px; line-height: 1.15;
    display: flex; flex-direction: column; justify-content: center;
    padding-left: 16px;
  }
</style>
</head>
<body>
<main class="canvas">

  <section class="card card--front" aria-label="Business card front">
    <h1 class="wordmark">
      <span class="wordmark__name">Halvern</span>
      <span class="wordmark__sub">Inspection Services, LLC</span>
    </h1>
    <div class="wordmark-rule"></div>
    <p class="contact">
      Dwayne Halvern<span class="contact__sep">|</span>(989) 517-2438<span class="contact__sep">|</span>halv7dw@mailtrove.net
    </p>
  </section>

  <section class="card card--back" aria-label="Business card back">
    <svg class="connector" viewBox="0 0 680 390" aria-hidden="true">
      <g fill="none" stroke="#e8692c" stroke-width="2">
        <path d="M0 168 H58"/>
        <path d="M78 105 H58 V232 H70"/>
      </g>
    </svg>
    <div class="cert cert--society">
      <div class="cert__title">NWB</div>
      <ul class="cert__list">
        <li>Certified Welding Inspector</li>
        <li>Certified Radiographic Interpreter</li>
        <li>Certified Welding Educator</li>
      </ul>
    </div>
    <div class="cert cert--level">
      <div class="cert__title">LEVEL II</div>
      <ul class="cert__list">
        <li>Ultrasonic Testing</li>
        <li>Magnetic Particle Testing</li>
        <li>Liquid Penetrant Testing</li>
      </ul>
    </div>
  </section>

</main>
</body>
</html>
```